Brightwell Systems - Company Overview Brochure

We would like a single page A4 Brochure to give to new potential customers to provide a quick overview of our company. This will be used in presales meetings.

We have included the content we would like on the brochure under "Brightwell Systems Marketing Brochure.docx".

We have included two other designs "timebundleterms v4.pdf and Brightwell Public Cloud Plans.pdf" which shows similar marketing brochures we have. We would like these designs to have the same Brightwell Blue and "Specialised Technology Consultancy firm" theme.

Target Market(s)

Technology Sector

Industry/Entity Type

Information Technology

Colors
0054AA
0677BA
7BADD7
CADEEF
E8F1F8

Requirements
Must have
• "Innovative Tech Company Theme".

```html
<!DOCTYPE html>
<html lang="en">
<head>
<meta charset="utf-8">
<title>Brightwell Systems – Company Overview Brochure</title>
<link href="https://fonts.googleapis.com/css2?family=Montserrat:wght@500;600;700&display=swap" rel="stylesheet">
<style>
  :root{
    --page-bg:#b9c3c6;
    --navy:#0b2a6b;
    --deep:#062466;
    --brand:#0054AA;
    --brand-mid:#0677BA;
    --sky:#7BADD7;
    --ice:#CADEEF;
    --mist:#E8F1F8;
    --white:#ffffff;
  }
  *{box-sizing:border-box;margin:0;padding:0}
  html,body{width:1200px;height:1036px;overflow:hidden;background:var(--page-bg);font-family:"Montserrat",sans-serif}
  .brochure{position:absolute;left:253px;top:28px;width:693px;height:980px;background:var(--white);overflow:hidden;box-shadow:0 4px 14px rgba(0,0,0,.25)}
  .header{position:absolute;left:0;top:0;width:693px;height:134px;background:var(--white)}
  .header-strip{position:absolute;left:438px;top:0;width:255px;height:11px;background:var(--deep)}
  .brand{position:absolute;left:40px;top:46px;display:flex;align-items:center;gap:12px;color:var(--navy);font-weight:700;font-size:29px;letter-spacing:.5px}
  .brand-mark{width:34px;height:34px;background:var(--brand)}
  .tagline{position:absolute;left:460px;top:36px;color:var(--navy);font-weight:600;font-size:34px;line-height:36px}
  .body{position:absolute;left:0;top:134px;width:693px;height:846px;background:radial-gradient(ellipse at 35% 35%,#1d6cc4 0%,#0c4aa0 40%,#062a72 100%)}
  .heading{position:absolute;left:40px;color:var(--white);font-weight:700;line-height:1.2}
  .overview-title{top:30px;font-size:24px}
  .overview-text{position:absolute;left:40px;top:68px;width:287px;color:var(--mist);font-size:13.5px;line-height:17px;text-align:justify;font-weight:500}
  .services-title{top:192px;font-size:25px}
  .service{position:absolute;width:150px;text-align:center;color:var(--white);font-weight:600;font-size:15px;line-height:18px}
  .service svg{display:block;margin:0 auto 6px}
  .commitment-title{top:652px;font-size:26px}
  .policy-title{top:700px;font-size:24px}
  .policy-text{position:absolute;left:40px;top:737px;width:290px;color:var(--mist);font-size:13.5px;line-height:17px;text-align:justify;font-weight:500}
  .slogan{position:absolute;left:350px;top:800px;transform-origin:0 0;transform:rotate(-90deg);white-space:nowrap;color:var(--sky);opacity:.65;font-weight:700;font-size:68px;line-height:68px}
  .photo{position:absolute;left:438px;width:255px}
  .photo-cloud{top:0;height:160px;background:linear-gradient(135deg,#0a2a5c,#2c6fb0 55%,#0d2f66)}
  .photo-security{top:162px;height:164px;background:linear-gradient(135deg,#0b2550,#1f76b6 50%,#0b2a5e)}
  .photo-transform{top:328px;height:163px;background:linear-gradient(135deg,#1d3a66,#3a78b2 50%,#142a50)}
  .photo-network{top:493px;height:158px;background:linear-gradient(135deg,#0e2b5a,#4a8cc4 50%,#1a3560)}
  .contact{position:absolute;left:437px;top:682px;width:240px;color:var(--white)}
  .contact-title{font-weight:700;font-size:21px;margin-bottom:8px;white-space:nowrap}
  .contact-item{display:flex;align-items:center;gap:7px;font-size:13px;line-height:23px;font-weight:500;white-space:nowrap}
  .contact-item svg{flex:none}
</style>
</head>
<body>
<main class="brochure">
  <header class="header">
    <div class="header-strip"></div>
    <div class="brand"><span class="brand-mark"></span>Brightwell Systems</div>
    <div class="tagline">Specialised<br>Consulting</div>
  </header>

  <section class="body">
    <h2 class="heading overview-title">Company Overview</h2>
    <p class="overview-text">An Australian company specializing in enterprise infrastructure, cybersecurity, networks, system infrastructure, cybersecurity, cloud, and strategic consulting, solution, professional, and professional branded team</p>

    <h2 class="heading services-title">Services Overview</h2>

    <div class="service" style="left:30px;top:240px">
      <svg width="64" height="74" viewBox="0 0 64 74"><path d="M32 3 L59 13 V36 C59 54 46 66 32 71 C18 66 5 54 5 36 V13 Z" fill="#4aa3e0" stroke="#CADEEF" stroke-width="3"/><rect x="21" y="33" width="22" height="18" rx="3" fill="#062a72"/><path d="M25 33 V27 a7 7 0 0 1 14 0 V33" fill="none" stroke="#062a72" stroke-width="4"/></svg>
      Cybersecurity
    </div>
    <div class="service" style="left:181px;top:244px">
      <svg width="80" height="70" viewBox="0 0 80 70"><path d="M20 42 a14 14 0 0 1 2-28 a18 18 0 0 1 34 2 a13 13 0 0 1 4 26 Z" fill="#ffffff"/><rect x="28" y="22" width="24" height="7" fill="#7BADD7"/><rect x="28" y="31" width="24" height="7" fill="#7BADD7"/><rect x="28" y="40" width="24" height="7" fill="#7BADD7"/><line x1="40" y1="47" x2="40" y2="60" stroke="#7BADD7" stroke-width="2"/><line x1="22" y1="60" x2="58" y2="60" stroke="#7BADD7" stroke-width="2"/><circle cx="40" cy="60" r="3" fill="#4aa3e0"/></svg>
      Cloud Solutions
    </div>

    <div class="service" style="left:30px;top:366px">
      <svg width="66" height="76" viewBox="0 0 66 76"><path d="M32 3 L58 13 V36 C58 54 45 66 32 71 C19 66 6 54 6 36 V13 Z" fill="#4aa3e0" stroke="#CADEEF" stroke-width="3"/><path d="M22 34 a10 10 0 0 1 18-6" fill="none" stroke="#062a72" stroke-width="4"/><path d="M42 38 a10 10 0 0 1 -18 6" fill="none" stroke="#062a72" stroke-width="4"/><path d="M46 56 a10 10 0 1 0 6 -8" fill="none" stroke="#CADEEF" stroke-width="3"/></svg>
      Business<br>Continuity
    </div>
    <div class="service" style="left:181px;top:370px">
      <svg width="80" height="76" viewBox="0 0 80 76"><circle cx="38" cy="20" r="11" fill="#ffe38a"/><rect x="33" y="31" width="10" height="6" fill="#CADEEF"/><circle cx="60" cy="20" r="7" fill="none" stroke="#4aa3e0" stroke-width="4"/><rect x="6" y="38" width="24" height="7" fill="#CADEEF"/><rect x="6" y="47" width="24" height="7" fill="#CADEEF"/><rect x="6" y="56" width="24" height="7" fill="#CADEEF"/><rect x="48" y="44" width="24" height="18" rx="2" fill="none" stroke="#CADEEF" stroke-width="2.5"/><text x="60" y="58" font-family="Montserrat,sans-serif" font-size="10" font-weight="700" fill="#CADEEF" text-anchor="middle">VM</text><line x1="18" y1="68" x2="60" y2="68" stroke="#4aa3e0" stroke-width="2"/><circle cx="40" cy="68" r="3" fill="#4aa3e0"/></svg>
      Virtualisation
    </div>

    <div class="service" style="left:30px;top:504px">
      <svg width="74" height="74" viewBox="0 0 74 74"><g fill="#9ab3cc"><circle cx="37" cy="37" r="24"/><rect x="32" y="4" width="10" height="12"/><rect x="32" y="58" width="10" height="12"/><rect x="4" y="32" width="12" height="10"/><rect x="58" y="32" width="12" height="10"/><rect x="32" y="4" width="10" height="12" transform="rotate(45 37 37)"/><rect x="32" y="58" width="10" height="12" transform="rotate(45 37 37)"/><rect x="4" y="32" width="12" height="10" transform="rotate(45 37 37)"/><rect x="58" y="32" width="12" height="10" transform="rotate(45 37 37)"/></g><circle cx="37" cy="37" r="10" fill="#0c4aa0"/><path d="M26 26 L56 58" stroke="#4aa3e0" stroke-width="7" stroke-linecap="round"/></svg>
      Managed<br>Services
    </div>
    <div class="service" style="left:181px;top:504px">
      <svg width="80" height="74" viewBox="0 0 80 74"><rect x="42" y="4" width="30" height="44" fill="none" stroke="#4aa3e0" stroke-width="2.5"/><path d="M48 14 h12 v10 h8 M50 32 h14" stroke="#4aa3e0" stroke-width="2" fill="none"/><rect x="10" y="26" width="22" height="44" fill="#CADEEF"/><rect x="32" y="18" width="20" height="52" fill="#ffffff"/><g fill="#0c4aa0"><rect x="14" y="32" width="5" height="5"/><rect x="23" y="32" width="5" height="5"/><rect x="14" y="42" width="5" height="5"/><rect x="23" y="42" width="5" height="5"/><rect x="14" y="52" width="5" height="5"/><rect x="23" y="52" width="5" height="5"/><rect x="36" y="24" width="5" height="5"/><rect x="44" y="24" width="5" height="5"/><rect x="36" y="34" width="5" height="5"/><rect x="44" y="34" width="5" height="5"/><rect x="36" y="44" width="5" height="5"/><rect x="44" y="44" width="5" height="5"/><rect x="36" y="54" width="5" height="5"/><rect x="44" y="54" width="5" height="5"/></g><line x1="6" y1="70" x2="60" y2="70" stroke="#ffffff" stroke-width="2"/></svg>
      Enterprise<br>Architecture
    </div>

    <h2 class="heading commitment-title">Our Commitment</h2>
    <h3 class="heading policy-title">Our Policy</h3>
    <p class="policy-text">Corporate policies are lude commits to policies and results and resul to quality, sustainability, manparies, e.g., security, sustainability, and saw, etc.</p>

    <div class="slogan">Do it Once, Do it Right</div>

    <div class="photo photo-cloud" role="img" aria-label="Photo of a server room with a glowing cloud and server icon"></div>
    <div class="photo photo-security" role="img" aria-label="Photo of a hand holding a glowing security shield icon in front of server racks"></div>
    <div class="photo photo-transform" role="img" aria-label="Photo of a businessman touching a digital transformation interface"></div>
    <div class="photo photo-network" role="img" aria-label="Photo of a data centre with a network of connected security icons"></div>

    <div class="contact">
      <div class="contact-title">Contact Information</div>
      <div class="contact-item"><svg width="13" height="13" viewBox="0 0 24 24"><path d="M6 2 L10 7 L8 10 C9 13 11 15 14 16 L17 14 L22 18 L19 22 C10 21 3 14 2 5 Z" fill="#4aa3e0"/></svg>+61 2 9000 4821</div>
      <div class="contact-item"><svg width="13" height="13" viewBox="0 0 24 24"><rect x="2" y="5" width="20" height="14" fill="#4aa3e0"/><path d="M2 5 L12 13 L22 5" fill="none" stroke="#062a72" stroke-width="2"/></svg>info@brightwellsystems.com.au</div>
      <div class="contact-item"><svg width="13" height="13" viewBox="0 0 24 24"><path d="M12 2 a7 7 0 0 1 7 7 c0 5-7 13-7 13 s-7-8-7-13 a7 7 0 0 1 7-7Z" fill="#4aa3e0"/><circle cx="12" cy="9" r="2.5" fill="#062a72"/></svg>Sydney, Australia</div>
      <div class="contact-item"><svg width="13" height="13" viewBox="0 0 24 24"><circle cx="12" cy="12" r="9" fill="none" stroke="#4aa3e0" stroke-width="2"/><ellipse cx="12" cy="12" rx="4" ry="9" fill="none" stroke="#4aa3e0" stroke-width="2"/><line x1="3" y1="12" x2="21" y2="12" stroke="#4aa3e0" stroke-width="2"/></svg>brightwellsystems.com.au</div>
    </div>
  </section>
</main>
</body>
</html>
```